Ready to Run a Venture? Podcast

We need a "Podcast Cover" for inclusion on Vexora and brightreef along with a matching or complimentary banner to be included on a landing page which will be hosted on Plinkfern (a Plinkfern template). The Podcast is called the "Ready to Run a Venture?" Podcast and has a tag line of "listen before you leap".

I've included an image for a bit of inspiration that shows a person ready to leap into the unknown which, in our podcast, is like a metaphor for launching a business. You may use the photo in your design if you wish or do something completely different including "cartoon" characters or simply text.

Target Market(s)

People who are thinking about starting a new business or buying an existing business and whom have never owned a business before.

Industry/Entity Type

Startup

Font styles to use
Sans Serif

Colors

Designer to choose colors to be used in the design.

Requirements
Must have
• incorporate the "listen before you leap" tagline.

```html
<!DOCTYPE html>
<html lang="en">
<head>
<meta charset="utf-8">
<title>Ready to Run a Venture? Podcast Cover</title>
<link rel="stylesheet" href="https://fonts.googleapis.com/css2?family=Open+Sans:wght@400;700&display=swap">
<style>
  :root {
    --paper: #ffffff;
    --sky-top: #66665b;
    --sky-mid: #8f8873;
    --sky-warm: #ada083;
    --sky-light: #d3d0ca;
    --rock: rgba(22, 20, 18, 0.95);
    --rock-fade: rgba(22, 20, 18, 0);
    --shade: rgba(30, 28, 24, 0.35);
    --shade-fade: rgba(30, 28, 24, 0);
    --ink-light: #ffffff;
  }
  html, body {
    margin: 0;
    padding: 0;
    width: 1200px;
    height: 1200px;
    overflow: hidden;
    background: var(--paper);
  }
  .cover {
    position: relative;
    width: 1200px;
    height: 1200px;
    background: var(--paper);
    font-family: "Open Sans", Arial, sans-serif;
  }
  .cover__scene {
    position: absolute;
    left: 8px;
    top: 8px;
    width: 1184px;
    height: 1184px;
    overflow: hidden;
    background:
      radial-gradient(ellipse 200px 300px at 90px 1120px, var(--rock) 0%, var(--rock) 45%, var(--rock-fade) 100%),
      radial-gradient(ellipse 260px 320px at 1110px 1100px, var(--rock) 0%, var(--rock) 45%, var(--rock-fade) 100%),
      radial-gradient(ellipse 240px 460px at 600px 480px, var(--shade) 0%, var(--shade-fade) 100%),
      radial-gradient(circle at 96% 76%, var(--sky-light) 0%, rgba(211, 208, 202, 0) 30%),
      linear-gradient(170deg, var(--sky-top) 0%, var(--sky-mid) 40%, var(--sky-warm) 72%, var(--sky-mid) 100%);
  }
  .cover__marks {
    position: absolute;
    inset: 0;
  }
  .cover__marks line {
    stroke: var(--ink-light);
    stroke-width: 8;
  }
  .cover__title {
    position: absolute;
    left: 252px;
    top: 330px;
    margin: 0;
    color: var(--ink-light);
    font-weight: 700;
    font-size: 128px;
    line-height: 172px;
    letter-spacing: -1px;
    text-transform: uppercase;
  }
  .cover__title span {
    display: block;
    white-space: nowrap;
  }
  .cover__tagline {
    position: absolute;
    left: 307px;
    top: 852px;
    margin: 0;
    color: var(--ink-light);
    font-weight: 400;
    font-size: 50px;
    line-height: 60px;
    white-space: nowrap;
  }
</style>
</head>
<body>
  <main class="cover">
    <div class="cover__scene" role="img" aria-label="Silhouette of a person leaping across a gap between two dark rocky cliffs against a hazy evening sky"></div>

    <svg class="cover__marks" width="1200" height="1200" viewBox="0 0 1200 1200" aria-hidden="true">
      <line x1="53" y1="56" x2="161" y2="154"/>
      <line x1="1046" y1="154" x2="1157" y2="56"/>
      <line x1="65" y1="1147" x2="176" y2="1048"/>
      <line x1="1046" y1="1048" x2="1155" y2="1147"/>
    </svg>

    <h1 class="cover__title">
      <span>Ready to</span>
      <span>Run a</span>
      <span>Venture?</span>
    </h1>
    <p class="cover__tagline">Listen before you leap</p>
  </main>
</body>
</html>
```